Brindle Structures Construction Company Seeking Modern Website

We are a small construction company wanting to create a web presence. We don't have much in the way of current content but will get photos as they come in. Attached is a picture of our business card.
The pages we would like on the menu are:
Home
Portfolio
Product Specs
Testimonials
Our Process
Contact
Some designs we like are:
http://www.tovenquarnsheds.example/
http://www.qzrsheds.example/
http://pannowsheds.example/
http://wistenhalls.example/
Not much requirements other than that so feel free to be creative!
Updates
Target Market(s)
Construction
Commercial and Residential Buildings
Industry/Entity Type
Construction Company
Number of Pages Required
5+ page
Look and feel

```html
<!DOCTYPE html>
<html lang="en">
<head>
<meta charset="utf-8">
<title>Brindle Structures — Home</title>
<link href="https://fonts.googleapis.com/css2?family=Open+Sans:wght@400;600;700&display=swap" rel="stylesheet">
<style>
:root{
  --red:#e8392b;
  --red-soft:#f04a3c;
  --ink:#2b2b2b;
  --muted:#8a8a8a;
  --line:#dcdcdc;
  --blue:#3fb3ea;
  --header-bg:#f4f6fb;
  --footer:#1f1f1f;
  --footer-base:#141414;
  --footer-text:#bdbdbd;
  --white:#ffffff;
}
*{box-sizing:border-box;margin:0;padding:0}
html,body{width:780px;height:1200px;overflow:hidden}
body{position:relative;background:var(--white);font-family:"Open Sans",Arial,sans-serif;color:var(--ink)}
.abs{position:absolute}

/* header */
.site-header{left:0;top:0;width:780px;height:70px;background:var(--header-bg);border-bottom:1px solid #c9ced8}
.brand{left:62px;top:20px;display:flex;align-items:center;gap:6px}
.brand-mark{width:12px;height:12px;background:var(--red)}
.brand-name{font-size:13px;font-weight:700;color:var(--red)}
.main-nav{left:251px;top:33px;display:flex;font-size:10.5px}
.main-nav a{color:var(--ink);text-decoration:none;height:23px;line-height:21px;padding:0 14px;border:1px solid transparent;margin-right:2px}
.main-nav a.current{border-color:var(--red)}
.main-nav a:nth-child(2){margin-left:2px}

/* hero */
.hero{left:0;top:70px;width:780px;height:299px;background:linear-gradient(180deg,#9fb3c6 0%,#c9b7a0 45%,#8c7a64 72%,#4d6b36 100%)}
.hero-title{left:116px;top:174px;width:536px;height:43px;background:var(--red);color:var(--white);font-size:24.5px;font-weight:600;text-align:center;line-height:43px}
.hero-sub{left:212px;top:229px;width:354px;height:29px;background:rgba(40,40,40,.85);color:var(--white);font-size:11.5px;text-align:center;line-height:29px}

/* services */
.section-rule{height:1px;background:var(--line)}
.services-title{left:0;top:400px;width:780px;text-align:center;font-size:27px;font-weight:600;letter-spacing:.5px}
.services-title span{background:var(--white);padding:0 8px}
.card{top:458px;width:152px;height:220px;background:var(--white);box-shadow:0 1px 3px rgba(0,0,0,.18)}
.card-photo{height:93px;border-bottom:2px solid var(--blue)}
.card-badge{left:67px;top:84px;width:18px;height:18px}
.card-title{position:absolute;left:0;top:106px;width:152px;text-align:center;font-size:13.5px;letter-spacing:.3px}
.card-text{position:absolute;left:7px;top:138px;width:138px;font-size:7.6px;line-height:13px;color:var(--muted)}
.card-more{position:absolute;left:8px;top:196px;width:136px;border-top:1px solid #ececec;padding-top:4px;text-align:center;font-size:11px;color:var(--red-soft)}

/* welcome */
.welcome-title{left:0;top:718px;width:780px;text-align:center;font-size:28px;letter-spacing:2px}
.welcome-rule{left:152px;top:762px;width:497px;height:1px;background:var(--line)}
.welcome-accent{left:327px;top:762px;width:96px;height:3px;background:var(--red)}
.welcome-copy{left:70px;top:784px;width:640px;text-align:center;font-size:9.6px;line-height:14.5px;color:#444}
.welcome-copy p{margin-bottom:14px}
.btn-outline{left:315px;top:891px;width:105px;height:27px;border:1px solid #bbb;border-radius:2px;text-align:center;line-height:25px;font-size:9.5px;color:#555}

/* footer */
.site-footer{left:0;top:954px;width:780px;height:222px;background:var(--footer)}
.footer-base{left:0;top:1176px;width:780px;height:24px;background:var(--footer-base);color:#9a9a9a;font-size:7.5px;text-align:center;line-height:24px;letter-spacing:.3px}
.footer-brand{left:78px;top:982px;display:flex;align-items:center;gap:5px}
.footer-brand .brand-mark{background:#9a9a9a;width:10px;height:10px}
.footer-brand .brand-name{color:#9a9a9a;font-size:11px}
.footer-about{left:64px;top:1028px;width:140px;font-size:7.6px;line-height:13.2px;color:var(--footer-text)}
.social{left:66px;top:1108px;display:flex;gap:5px}
.social span{width:20px;height:20px;border-radius:50%;background:var(--red)}
.footer-heading{font-size:10.5px;font-weight:700;color:var(--white);letter-spacing:-.2px}
.comment{position:absolute;left:0;width:146px;font-size:7.4px;color:var(--white);font-weight:600;letter-spacing:-.2px}
.comment em{font-style:normal;color:#777;font-weight:400}
.comment-divider{position:absolute;left:0;width:146px;height:1px;background:#333}
.tweet{position:absolute;left:0;width:146px;font-size:7.4px;line-height:13px;color:#aaa;padding-left:17px}
.tweet b{color:var(--white);font-weight:600}
.tweet .tweet-link{color:var(--white);font-weight:600}
.tweet-dot{position:absolute;left:0;top:3px;width:7px;height:7px;background:var(--red);border-radius:1px}
.post{position:absolute;left:0;width:150px;height:40px}
.post-thumb{position:absolute;left:0;top:0;width:49px;height:37px;background:linear-gradient(160deg,#a9c3d8,#e8ecef 55%,#6c8a5a)}
.post-title{position:absolute;left:59px;top:0;width:92px;font-size:7.3px;font-weight:600;color:var(--white);line-height:9px;letter-spacing:-.2px}
.post-meta{position:absolute;left:59px;font-size:6.6px;color:#aaa;font-style:italic;font-family:Georgia,serif}
.post-meta b{color:var(--white);font-style:normal;margin-left:4px}
.post-meta i{display:inline-block;width:7px;height:4px;border:1px solid var(--red);border-radius:50%;margin-left:4px;vertical-align:middle}
</style>
</head>
<body>

<header class="site-header abs">
  <div class="brand abs"><span class="brand-mark"></span><span class="brand-name">Brindle Structures</span></div>
  <nav class="main-nav abs">
    <a class="current">Home</a><a>Portfolio</a><a>Product Specs</a><a>Testimonials</a><a>Our Process</a><a>Contact</a>
  </nav>
</header>

<section class="hero abs" role="img" aria-label="Two-storey family home with grey siding, white garage doors and a front lawn at dusk"></section>
<h1 class="hero-title abs">Self Managed Super Funds-IT's your Future</h1>
<p class="hero-sub abs">Take control of your super &amp; Buy Investment Properties</p>

<div class="section-rule abs" style="left:62px;top:421px;width:653px"></div>
<h2 class="services-title abs"><span>Our Services</span></h2>

<article class="card abs" style="left:64px">
  <div class="card-photo" role="img" aria-label="Bright apartment bedroom with white bed and television" style="background:linear-gradient(135deg,#5a3b2c,#c9b9a8 50%,#3a2a22)"></div>
  <svg class="card-badge abs" viewBox="0 0 18 18"><rect x="3" y="3" width="12" height="12" transform="rotate(45 9 9)" fill="var(--blue)"/><path d="M9 5.5l1 2.2 2.3.2-1.8 1.5.6 2.3L9 10.4l-2.1 1.3.6-2.3-1.8-1.5 2.3-.2z" fill="none" stroke="#fff" stroke-width=".8"/></svg>
  <h3 class="card-title">Property Management</h3>
  <p class="card-text">Beautiful, updated, ground level Co-op apartment in the desirable Bay Terrace neighborhood. This home ...</p>
  <div class="card-more">Read More ›</div>
</article>

<article class="card abs" style="left:230px">
  <div class="card-photo" role="img" aria-label="Mediterranean style villa with terracotta roof and garden" style="background:linear-gradient(180deg,#7fb3e0,#c99a6a 55%,#5f8a3a)"></div>
  <svg class="card-badge abs" viewBox="0 0 18 18"><rect x="3" y="3" width="12" height="12" transform="rotate(45 9 9)" fill="var(--blue)"/><path d="M9 5.5l1 2.2 2.3.2-1.8 1.5.6 2.3L9 10.4l-2.1 1.3.6-2.3-1.8-1.5 2.3-.2z" fill="none" stroke="#fff" stroke-width=".8"/></svg>
  <h3 class="card-title">NRAS Properties</h3>
  <p class="card-text">Just steps away from QM2 express bus to Manhattan and local buses; only minutes ...</p>
  <div class="card-more">Read More ›</div>
</article>

<article class="card abs" style="left:396px">
  <div class="card-photo" role="img" aria-label="Historic waterfront buildings reflected in a canal" style="background:linear-gradient(180deg,#5d6d80,#8a6e55 50%,#3b3f48)"></div>
  <svg class="card-badge abs" viewBox="0 0 18 18"><rect x="3" y="3" width="12" height="12" transform="rotate(45 9 9)" fill="var(--blue)"/><path d="M9 5.5l1 2.2 2.3.2-1.8 1.5.6 2.3L9 10.4l-2.1 1.3.6-2.3-1.8-1.5 2.3-.2z" fill="none" stroke="#fff" stroke-width=".8"/></svg>
  <h3 class="card-title" style="top:104px">Sale for Properties</h3>
  <p class="card-text">Mineral Reserves: 2008 core drilling and testing (on just 60 of the 1,100 acres) ...</p>
  <div class="card-more">Read More ›</div>
</article>

<article class="card abs" style="left:562px">
  <div class="card-photo" role="img" aria-label="Stone manor house surrounded by green trees" style="background:linear-gradient(180deg,#b9d3e8,#b8b3a4 50%,#4f7a32)"></div>
  <svg class="card-badge abs" viewBox="0 0 18 18"><rect x="3" y="3" width="12" height="12" transform="rotate(45 9 9)" fill="var(--blue)"/><path d="M9 5.5l1 2.2 2.3.2-1.8 1.5.6 2.3L9 10.4l-2.1 1.3.6-2.3-1.8-1.5 2.3-.2z" fill="none" stroke="#fff" stroke-width=".8"/></svg>
  <h3 class="card-title">Properties for Rent</h3>
  <p class="card-text">This property is mostly wooded and sits high on a hilltop overlooking the Mohawk ...</p>
  <div class="card-more">Read More ›</div>
</article>

<h2 class="welcome-title abs">WELCOME TO PERTH</h2>
<div class="welcome-rule abs"></div>
<div class="welcome-accent abs"></div>
<div class="welcome-copy abs">
  <p>The team at Kestrel Property Solutions are devoted to finding new methods of selling property and have an extraordinarily creative approach to this. Unlike other agents once we have secured your business our work actually begins.</p>
  <p>Our team of experts are ready to provide support and information to make your journey easy and profitable.</p>
  <p>Experience success!&nbsp; Talk to your Kestrel Property Solutions guru today.</p>
</div>
<div class="btn-outline abs">Read More &nbsp;››</div>

<footer class="site-footer abs"></footer>
<div class="footer-brand abs"><span class="brand-mark"></span><span class="brand-name">Brindle Structures</span></div>
<p class="footer-about abs">This is the perfect four bedroom family home on an idyllic block, in one of Chicago's nicest suburbs. With three bedrooms and a master suite, there is plenty of space for all.</p>
<div class="social abs"><span></span><span></span><span></span><span></span><span></span></div>

<div class="abs" style="left:226px;top:984px;width:150px">
  <h4 class="footer-heading">Recent Comments</h4>
  <div class="comment" style="top:30px">Admin <em>on</em> Is Condo Life For You?</div>
  <div class="comment-divider" style="top:53px"></div>
  <div class="comment" style="top:66px">Admin <em>on</em> New Post With Image</div>
  <div class="comment-divider" style="top:88px"></div>
  <div class="comment" style="top:101px">Admin <em>on</em> House Market Indicators</div>
  <div class="comment-divider" style="top:124px"></div>
  <div class="comment" style="top:137px">Tom Ashby <em>on</em> Is Condo Life For You?</div>
</div>

<div class="abs" style="left:388px;top:984px;width:150px">
  <h4 class="footer-heading">Chirpline</h4>
  <div class="tweet" style="top:28px"><span class="tweet-dot"></span><b>@Studio_Vantor</b> Looking Ahead: Trendy #blogger and #portfolio Site #Templates in Production! <span class="tweet-link">vantorstudio.example/looking-ahead-...</span></div>
  <div class="comment-divider" style="top:91px;left:17px;width:129px"></div>
  <div class="tweet" style="top:103px"><span class="tweet-dot"></span><b>@Studio_Vantor</b> Congrats my dear friend, wish you lots of inspiration to attain much more! <span class="tweet-link">chirpline.example/orvelle/st...</span></div>
</div>

<div class="abs" style="left:550px;top:984px;width:160px">
  <h4 class="footer-heading">Recent Posts</h4>
  <div class="post" style="top:28px">
    <div class="post-thumb" role="img" aria-label="Modern white house with glass facade"></div>
    <div class="post-title">NEW POST WITH IMAGE</div>
    <div class="post-meta" style="top:18px">January 6, 2015<i></i><b>643</b></div>
  </div>
  <div class="post" style="top:83px">
    <div class="post-thumb" role="img" aria-label="Contemporary house on a hillside"></div>
    <div class="post-title">HOUSE MARKET INDICATORS</div>
    <div class="post-meta" style="top:24px">December 10, 2014<br><i style="margin-left:2px"></i><b>466</b></div>
  </div>
  <div class="post" style="top:138px">
    <div class="post-thumb" role="img" aria-label="Modern house with pool" style="background:linear-gradient(160deg,#e9eef1,#b88a5a 55%,#3fa0c9)"></div>
    <div class="post-title">POST WITH IMAGE</div>
    <div class="post-meta" style="top:17px">December 8, 2014<i></i><b>92</b></div>
  </div>
</div>

<div class="footer-base abs">© 2015 BRINDLE STRUCTURES, ALL RIGHTS RESERVED.</div>

</body>
</html>
```